Brannigan Schedule Oversight Group Inc. needs a logo design (BSOGI) and a business card design

We need a logo design and business card design for a new company. Simple yet elegant/stylish and professional. to the point. Focal point BRANNIGAN...underneith Schedule Oversight Group Inc smaller font. Plus a logo that can be on the opposite side of the business card and used for T-Shirts.
Back back ground, silver/grey font. I like the look of QVR Design logo
Target Market(s)
Project controls, Planning, Scheduling, Engineering, Project Management
Industry/Entity Type
Business
Contact Information for Business Card
Company name on one side, logo and details on the other
Font styles to use
Requirements
Must have
- Rosalind Brannigan
- Project Planner
- BranniganSOGI@mailnest.example
- P.O. Box 7
- Harrowdale WL NORTHIA
- T0M2J3
- +1 (403) 555 0187
Nice to have
- Your input :) quote "Fail to plan, plan to fail"
Should not have
- Too much!

```html
<!DOCTYPE html>
<html lang="en">
<head>
<meta charset="utf-8">
<title>Brannigan Schedule Oversight Group – Business Card</title>
<link rel="stylesheet" href="https://fonts.googleapis.com/css2?family=Arimo:ital,wght@0,400;0,700;1,400&display=swap">
<style>
  :root {
    --backdrop: #b5b7b8;
    --card-dark: #3d3d3f;
    --card-light: #ffffff;
    --silver: #e2e2e2;
    --ink: #5a5a5c;
    --ink-soft: #6b6b6d;
  }
  * { margin: 0; padding: 0; box-sizing: border-box; }
  html, body {
    width: 1200px; height: 852px; overflow: hidden;
    background: var(--backdrop);
    font-family: "Arimo", Arial, sans-serif;
  }
  .canvas { position: relative; width: 1200px; height: 852px; }
  .card {
    position: absolute; top: 289px; width: 447px; height: 273px;
    border-radius: 14px;
  }
  .card--front { left: 134px; background: var(--card-dark); }
  .card--back { left: 613px; background: var(--card-light); color: var(--ink); }

  .front-mark {
    position: absolute; left: 202px; top: 98px; width: 42px; height: 42px;
    border: 1.5px solid var(--silver); border-radius: 50%;
  }
  .front-name {
    position: absolute; left: 0; right: 0; top: 139px; text-align: center;
    color: var(--silver); font-size: 20px; font-weight: 400;
    letter-spacing: 12px; padding-left: 12px;
  }
  .front-tagline {
    position: absolute; left: 0; right: 0; top: 175px; text-align: center;
    color: var(--silver); font-size: 6.5px; font-weight: 700;
    letter-spacing: 3.6px; padding-left: 3.6px;
  }

  .back-mark {
    position: absolute; left: 25px; top: 27px; width: 40px; height: 40px;
    border: 1.5px solid var(--ink-soft); border-radius: 50%;
  }
  .holder { position: absolute; right: 28px; top: 30px; text-align: right; }
  .holder__name { font-size: 14px; font-weight: 700; line-height: 16px; letter-spacing: 0.8px; }
  .holder__role { font-size: 12px; line-height: 15px; letter-spacing: 0.6px; }

  .contact { position: absolute; right: 25px; top: 147px; font-size: 12.5px; line-height: 23px; letter-spacing: 0.5px; }
  .contact__row { display: flex; justify-content: flex-end; align-items: flex-start; gap: 6px; }
  .contact__text { text-align: right; }
  .contact__address { line-height: 18.5px; padding-top: 2px; }
  .contact__icon { width: 18px; height: 23px; display: flex; align-items: center; justify-content: center; flex: none; }
  .contact__icon svg { fill: var(--ink-soft); }

  .motto {
    position: absolute; left: 23px; top: 231px;
    font-size: 13px; font-style: italic; color: var(--ink-soft);
    letter-spacing: 0.8px;
  }
</style>
</head>
<body>
<main class="canvas">
  <section class="card card--front" aria-label="Card front">
    <div class="front-mark"></div>
    <p class="front-name">BRANNIGAN</p>
    <p class="front-tagline">SCHEDULE OVERSIGHT GROUP</p>
  </section>

  <section class="card card--back" aria-label="Card back">
    <div class="back-mark"></div>
    <div class="holder">
      <p class="holder__name">Rosalind Brannigan</p>
      <p class="holder__role">Project Planner</p>
    </div>
    <div class="contact">
      <div class="contact__row">
        <span class="contact__text">+1 (403) 555 0187</span>
        <span class="contact__icon"><svg width="15" height="15" viewBox="0 0 24 24"><path d="M6.6 10.8a15.1 15.1 0 0 0 6.6 6.6l2.2-2.2c.3-.3.7-.4 1-.2 1.1.4 2.3.6 3.6.6.6 0 1 .4 1 1V20c0 .6-.4 1-1 1C10.6 21 3 13.4 3 4c0-.6.4-1 1-1h3.5c.6 0 1 .4 1 1 0 1.3.2 2.5.6 3.6.1.3 0 .7-.2 1z"/></svg></span>
      </div>
      <div class="contact__row">
        <span class="contact__text">BranniganSOGI@mailnest.example</span>
        <span class="contact__icon"><svg width="17" height="12" viewBox="0 0 24 17"><path d="M0 0h24v2L12 10 0 2z"/><path d="M0 4.5l12 8 12-8V17H0z"/></svg></span>
      </div>
      <div class="contact__row">
        <span class="contact__text contact__address">P.O. Box 7<br>Harrowdale WL NORTHIA,<br>T0M2J3</span>
        <span class="contact__icon"><svg width="12" height="16" viewBox="0 0 12 17"><path d="M6 0a6 6 0 0 0-6 6c0 4.5 6 11 6 11s6-6.5 6-11a6 6 0 0 0-6-6zm0 8.3A2.3 2.3 0 1 1 6 3.7a2.3 2.3 0 0 1 0 4.6z"/></svg></span>
      </div>
    </div>
    <p class="motto">“Fail to plan, plan to fail”</p>
  </section>
</main>
</body>
</html>
```